Tarn Studio PPT design

We are looking for a fresh and funky PPT design that is both eye-catching and allows room/whitespace for us to get the content across. We are a social media agency based in China and our logo although simple sort of reflects the nature of the company. There are two main tasks for this PPT, one as a business card to show-case our case-studies, but also as a back-drop to our pitch presentations and other client presentations. These presentations are a mix of visuals, text and graphs. The key message we want to get across is that we are professional, creative and fresh. We think that using our four support colours may work but are open to suggestions.
Current website www.tarnasia-example.com
Reason: Hi All,
as we have just guaranteed the payment we extended the deadline to allow for more submissions. Please bear with us.
Thanks,
Tarn Studio Team
Reason: To see more designs, we extend the deadline to March 18, 2014. Thanks.
Target Market(s)
Marketing CMO's, company CEO's, product managers, social media managers
Industry/Entity Type
Business

```html
<!DOCTYPE html>
<html lang="en">
<head>
<meta charset="utf-8">
<title>Tarn Studio – Presentation Template</title>
<link href="https://fonts.googleapis.com/css2?family=Arimo:ital,wght@0,400;0,700;1,400&display=swap" rel="stylesheet">
<style>
  :root {
    --canvas: #6fbffc;
    --white: #ffffff;
    --ink: #111111;
    --text: #333333;
    --purple: #7f44c4;
    --purple-deep: #6a2d99;
    --lavender: #d9d6fb;
    --lavender-soft: #e8e6fc;
    --green: #8cc63f;
    --pink: #e6358c;
    --orange: #f26a2e;
    --violet: #7b3fb5;
  }
  * { box-sizing: border-box; margin: 0; padding: 0; }
  html, body { width: 701px; height: 1200px; overflow: hidden; }
  body {
    background: var(--canvas);
    font-family: "Arimo", Arial, sans-serif;
    color: var(--text);
    position: relative;
  }
  .slide {
    position: absolute;
    left: 21px;
    width: 659px;
    height: 371px;
    background: var(--white);
    overflow: hidden;
  }
  .slide--cover { top: 21px; }
  .slide--who { top: 409px; }
  .slide--what { top: 797px; }

  /* Cover */
  .brand-name {
    position: absolute;
    font-weight: 700;
    color: var(--ink);
    letter-spacing: -0.5px;
    white-space: nowrap;
  }
  .slide--cover .brand-name { left: 60px; top: 74px; font-size: 34px; }
  .cover-title {
    position: absolute; left: 322px; top: 44px;
    font-size: 29px; line-height: 1.12; font-weight: 700; color: var(--ink);
  }
  .presenter { position: absolute; left: 323px; top: 139px; color: var(--purple-deep); }
  .presenter-name { font-size: 17.5px; }
  .presenter-role { font-size: 14px; font-style: italic; margin-top: 2px; }
  .cover-url { position: absolute; right: 17px; bottom: 12px; font-size: 11.5px; color: var(--ink); }
  .edge-tab { position: absolute; right: 0; top: 43px; }
  .cover-art {
    position: absolute; left: 0; bottom: 0; width: 280px; height: 170px;
    background: linear-gradient(90deg, rgba(140,198,63,.85) 0%, rgba(230,53,140,.85) 40%, rgba(123,63,181,.85) 60%, rgba(242,106,46,.85) 100%);
  }

  /* Content slides */
  .sidebar {
    position: absolute; left: 0; top: 0; width: 125px; height: 100%;
    background: var(--white);
  }
  .sidebar .brand-name { left: 0; width: 125px; text-align: center; top: 26px; font-size: 17px; }
  .nav { position: absolute; top: 94px; width: 125px; list-style: none; text-align: center; }
  .nav li { font-size: 12px; color: var(--ink); height: 31.5px; line-height: 15px; }
  .nav li.is-current { font-weight: 700; }
  .side-art {
    position: absolute; left: 0; bottom: 0; width: 140px; height: 56px;
    background: linear-gradient(90deg, rgba(140,198,63,.85) 0%, rgba(230,53,140,.85) 40%, rgba(123,63,181,.85) 60%, rgba(242,106,46,.85) 100%);
  }
  .pointer { position: absolute; left: 125px; width: 0; height: 0;
    border-top: 7px solid transparent; border-bottom: 7px solid transparent; border-left: 8px solid var(--white); }
  .main {
    position: absolute; left: 125px; top: 0; right: 0; bottom: 0;
    background: linear-gradient(160deg, var(--lavender) 60%, var(--lavender-soft) 100%);
  }
  .main-header {
    height: 70px; background: var(--purple);
    color: var(--white); font-size: 23px; font-weight: 700;
    padding: 26px 0 0 26px;
  }
  .lead { position: absolute; left: 26px; top: 92px; right: 10px; font-size: 14.6px; line-height: 20px; color: var(--text); }
  .point { position: absolute; left: 26px; right: 26px; display: flex; align-items: center; }
  .point-icon { flex: none; width: 39px; height: 39px; }
  .point-text { margin-left: 19px; font-size: 10.5px; line-height: 14.5px; color: var(--text); hyphens: auto; }
  .map-area {
    position: absolute; left: 26px; top: 146px; width: 484px; height: 201px;
    border: 3px solid var(--purple);
    background: linear-gradient(135deg, #ece9e2 0%, #e4e1da 50%, #d7e6c8 100%);
  }
</style>
</head>
<body>

<section class="slide slide--cover">
  <div class="brand-name">Tarn Studio</div>
  <h1 class="cover-title">This is the title<br>for our presentation!</h1>
  <div class="presenter">
    <p class="presenter-name">Lena Marsh</p>
    <p class="presenter-role">Digital Director – Partner</p>
  </div>
  <svg class="edge-tab" width="30" height="60" viewBox="0 0 30 60"><polygon points="30,0 0,30 30,60" fill="var(--violet)"/></svg>
  <div class="cover-art" role="img" aria-label="Decorative artwork in green, pink, purple and orange"></div>
  <p class="cover-url">www.tarnasia-example.com</p>
</section>

<section class="slide slide--who">
  <aside class="sidebar">
    <div class="brand-name">Tarn Studio</div>
    <ul class="nav">
      <li class="is-current">Who we are</li>
      <li>What we do</li>
      <li>How we work</li>
      <li>Contact Us</li>
      <li>More information</li>
    </ul>
    <div class="side-art" role="img" aria-label="Small decorative artwork in the brand colours"></div>
  </aside>
  <div class="main">
    <h2 class="main-header">Forever learning, forever pushing</h2>
    <p class="lead">We don't sit back on our laurels, we consistently push to learn and reapply ourselves to truly be able to add value to our clients' business</p>
    <div class="point" style="top:156px">
      <svg class="point-icon" viewBox="0 0 40 40"><circle cx="20" cy="20" r="20" fill="var(--violet)" opacity=".8"/><circle cx="16" cy="16" r="4" fill="#fff"/><path d="M9 28c0-5 3-7 7-7s7 2 7 7z" fill="#fff"/><circle cx="24" cy="15" r="3.5" fill="#fff"/><path d="M22 20c4 0 8 2 8 8h-6c0-4-1-6-2-8z" fill="#fff"/></svg>
      <p class="point-text">The Tarn Studio team are a group of dedicated professionals with varying areas of expertise. We believe we have found a great balance of strategists, project managers and content creators that can tackle most industries.</p>
    </div>
    <div class="point" style="top:228px">
      <svg class="point-icon" viewBox="0 0 40 40"><circle cx="20" cy="20" r="20" fill="var(--violet)" opacity=".8"/><circle cx="16" cy="16" r="4" fill="#fff"/><path d="M9 28c0-5 3-7 7-7s7 2 7 7z" fill="#fff"/><circle cx="24" cy="15" r="3.5" fill="#fff"/><path d="M22 20c4 0 8 2 8 8h-6c0-4-1-6-2-8z" fill="#fff"/></svg>
      <p class="point-text">The Tarn Studio team are a group of dedicated professionals with varying areas of expertise. We believe we have found a great balance of strategists, project managers and content creators that can tackle most industries.</p>
    </div>
    <div class="point" style="top:301px">
      <svg class="point-icon" viewBox="0 0 40 40"><circle cx="20" cy="20" r="20" fill="var(--violet)" opacity=".8"/><circle cx="16" cy="16" r="4" fill="#fff"/><path d="M9 28c0-5 3-7 7-7s7 2 7 7z" fill="#fff"/><circle cx="24" cy="15" r="3.5" fill="#fff"/><path d="M22 20c4 0 8 2 8 8h-6c0-4-1-6-2-8z" fill="#fff"/></svg>
      <p class="point-text">The Tarn Studio team are a group of dedicated professionals with varying areas of expertise. We believe we have found a great balance of strategists, project managers and content creators that can tackle most industries.</p>
    </div>
  </div>
  <span class="pointer" style="top:95px"></span>
</section>

<section class="slide slide--what">
  <aside class="sidebar">
    <div class="brand-name">Tarn Studio</div>
    <ul class="nav">
      <li>Who we are</li>
      <li class="is-current">What we do</li>
      <li>How we work</li>
      <li>Contact Us</li>
      <li>More information</li>
    </ul>
    <div class="side-art" role="img" aria-label="Small decorative artwork in the brand colours"></div>
  </aside>
  <div class="main">
    <h2 class="main-header">Understanding the market</h2>
    <p class="lead">Doing our homework helps us to determine how to move forward, efficiently, effectively and with purpose</p>
    <div class="map-area" role="img" aria-label="Street map of a city business district with a location pin"></div>
  </div>
  <span class="pointer" style="top:126px"></span>
</section>

</body>
</html>
```